Desk Allies Business Card

Contact Information for Business Card

Janne Voutilainen
Managing Director

3/47 Brindle Street Fernhill ACT 2915

Tel: +61 02 6257 3140
Mob: +61 0427 315 846

Email: janne@deskallies.com.au
Web: www.deskallies.com.au

Colors

Designer to choose colors to be used in the design.

Requirements
Must have
• Logo, Name, Title, Address, Telephone, Mobile, Email Address and Website
• "Desk Ally International Pty Ltd"

```html
<!DOCTYPE html>
<html lang="en">
<head>
<meta charset="utf-8">
<title>Desk Allies Business Card</title>
<link href="https://fonts.googleapis.com/css2?family=Open+Sans:wght@400;600;700&display=swap" rel="stylesheet">
<style>
  :root {
    --backdrop: #e9e6e1;
    --charcoal: #2c2c2d;
    --charcoal-light: #3a3a3c;
    --brand-blue: #1f74bd;
    --paper: #f7f7f6;
    --text-light: #e6e6e6;
    --text-grey: #7b7b7d;
  }
  * { margin: 0; padding: 0; box-sizing: border-box; }
  html, body {
    width: 1200px; height: 950px; overflow: hidden;
    background: var(--backdrop);
    font-family: "Open Sans", Arial, sans-serif;
  }
  .canvas {
    position: relative; width: 1200px; height: 950px;
    display: flex; align-items: center; justify-content: center; gap: 70px;
  }
  .card {
    box-shadow: 0 10px 28px rgba(0,0,0,.22);
    border-radius: 2px; overflow: hidden; position: relative;
  }
  /* Contact side */
  .card-front {
    width: 340px; height: 595px;
    background: var(--paper);
    display: flex; flex-direction: column;
  }
  .contact-panel {
    height: 300px;
    background: linear-gradient(160deg, var(--charcoal-light), var(--charcoal));
    padding: 40px 30px 0 30px;
    text-align: right;
    color: var(--text-light);
  }
  .person-name {
    color: var(--brand-blue); font-weight: 700; font-size: 21px;
    text-transform: uppercase; letter-spacing: .3px; line-height: 1.1;
  }
  .person-title {
    color: #fff; font-weight: 700; font-size: 16px;
    text-transform: uppercase; letter-spacing: .4px; margin-bottom: 14px;
  }
  .company, .address { font-size: 12.5px; line-height: 1.45; }
  .address { margin-bottom: 12px; }
  .contact-line { font-size: 15px; line-height: 1.4; }
  .brand-panel {
    flex: 1; display: flex; align-items: center; justify-content: center;
    border-top: 14px solid var(--brand-blue);
  }
  .brand-name-large {
    color: var(--brand-blue); font-weight: 700; font-size: 38px;
    text-transform: uppercase; letter-spacing: 1px;
  }
  /* Brand side */
  .card-back {
    width: 595px; height: 340px;
    background: var(--paper);
    display: flex; align-items: center; justify-content: center;
  }
  .lockup { display: flex; align-items: center; gap: 16px; }
  .brand-dot {
    width: 40px; height: 40px; border-radius: 50%;
    background: var(--charcoal);
  }
  .brand-name {
    color: var(--brand-blue); font-weight: 700; font-size: 38px;
    text-transform: uppercase; letter-spacing: 1px; line-height: 1;
  }
  .tagline {
    color: var(--text-grey); font-size: 12px; letter-spacing: 4.2px;
    text-transform: uppercase; margin-top: 6px;
  }
</style>
</head>
<body>
  <main class="canvas">
    <section class="card card-front">
      <div class="contact-panel">
        <p class="person-name">Janne Voutilainen</p>
        <p class="person-title">Managing Director</p>
        <p class="company">Desk Ally International Pty Ltd</p>
        <p class="address">3/47 Brindle Street Fernhill ACT 2915</p>
        <p class="contact-line">(P) +61 02 6257 3140</p>
        <p class="contact-line">(M) +61 0427 315 846</p>
        <p class="contact-line">janne@deskallies.com.au</p>
        <p class="contact-line">www.deskallies.com.au</p>
      </div>
      <div class="brand-panel">
        <p class="brand-name-large">Desk Allies</p>
      </div>
    </section>

    <section class="card card-back">
      <div class="lockup">
        <span class="brand-dot"></span>
        <div>
          <p class="brand-name">Desk Allies</p>
          <p class="tagline">Comfortable Workspace Design</p>
        </div>
      </div>
    </section>
  </main>
</body>
</html>
```